Computer consultant website

Vexlo Software is a newly started computer consulting company. It's a small one-man company that provides mostly Android applications but also websites in collaboration with designers. I'm running this company on the side of full time university studies.

I'm in need of a website which will function as:
Primarily - I'll direct potential clients to the page so they can read about the company, what i offer and past work.
Secondarily - Making my company visible through the web and maybe getting new clients.

The final design should look modern, clean and professional.

Pages that will be in the final website are (Note that it's not the exact titles as the page will not be in english):
* About
* Services (what Vexlo offers)
* Portfolio/work
* Short news (like PlanHives "News and press")
* Contact.

Inspiration
http://www.planhive.example/design/87836
http://www.brambleorb.example/
http://www.planhive.example/design/845881
http://www.planhive.example/design/1369424 - Lighter design, however a bit cluttered.

No programming code is needed delivered at all. Focus on designing rather then coding.

If you have any questions, do not hesitate to send me a message.

Target Market(s)

Non-technical entrepreneurs and small companies.

Industry/Entity Type

University

Requirements
Must have
• Must have my company logo (see attachment).

Must in any way use both colors from my logo.

A way to logically rearrange content to fit smaller screens. I will implement this design so that it can be pleasantly viewed on mobile devices. You don't necessarily need to provide exactly how the design would look on mobile devices.

I need the following types of page designs:
* Landing page
* Content page
* Portfolio/work (with accompanying inside/clicked) page

Landing/start page must in any way include at least the information:
* Shorter version of "About Vexlo"
* At least 1 most recent portfolio/work entry
* At least 1 most recent news entry
* Services that Vexlo offers.
Nice to have
Should not have
• Testimonials or newsletter.

```html
<!DOCTYPE html>
<html lang="en">
<head>
<meta charset="utf-8">
<title>Vexlo Software</title>
<link href="https://fonts.googleapis.com/css2?family=Carlito:wght@400;700&display=swap" rel="stylesheet">
<style>
:root{
  --canvas:#f1f1f1;
  --white:#ffffff;
  --ink:#2b2b2b;
  --muted:#555555;
  --blue:#2a7cf4;
  --blue-dark:#1c63d0;
  --line:#e2e2e2;
  --dark:#333031;
  --footer:#1b1a1a;
  --footer-text:#6d6d6d;
}
*{margin:0;padding:0;box-sizing:border-box}
html,body{width:1200px;height:900px;overflow:hidden}
body{background:var(--canvas);font-family:"Carlito",Calibri,Arial,sans-serif;color:var(--ink);position:relative}
.page{position:absolute;left:263px;top:11px;width:675px;height:879px;background:var(--white);overflow:hidden}

/* header */
.site-header{position:absolute;left:0;top:0;width:675px;height:58px;background:linear-gradient(#ffffff,#ececec);border-bottom:1px solid #dcdcdc}
.brand{position:absolute;left:84px;top:12px;display:flex;align-items:center;gap:7px}
.brand-dot{width:32px;height:32px;border-radius:50%;background:var(--blue)}
.brand-name{font-size:32px;font-weight:700;color:#2f2f2f;line-height:1;letter-spacing:-0.5px}
.main-nav{position:absolute;left:276px;top:0;height:58px;display:flex;border-left:1px solid #dadada}
.main-nav a{display:block;height:58px;line-height:58px;padding:0 9px;font-size:11px;color:#3a3a3a;text-decoration:none;border-right:1px solid #dadada;position:relative}
.main-nav a.active{background:linear-gradient(#45a0ff,var(--blue));color:#fff;border-color:var(--blue)}
.main-nav a.active::after{content:"";position:absolute;left:50%;bottom:-5px;margin-left:-5px;border:5px solid transparent;border-bottom:0;border-top-color:var(--blue)}

/* hero */
.hero{position:absolute;left:0;top:58px;width:675px;height:173px;background:#fff;overflow:hidden}
.hero-deco{position:absolute;left:0;top:0}
.hero-photo{position:absolute;left:30px;top:0;width:355px;height:173px;background:linear-gradient(90deg,#e9edf2 0%,#dfe3ea 40%,#3b4660 62%,#cfd4dc 85%,rgba(255,255,255,0) 100%)}
.hero-arrow{position:absolute;top:73px;width:22px;height:22px}
.hero-arrow.prev{left:28px}
.hero-arrow.next{left:624px}
.hero-copy{position:absolute;left:389px;top:56px;width:230px}
.hero-title{font-size:27px;font-weight:400;color:#2d2d2d;line-height:1}
.hero-title span{color:var(--blue)}
.hero-text{font-size:12.5px;color:#3a3a3a;line-height:15px;margin-top:3px}
.btn-more{position:absolute;left:540px;top:127px;width:59px;height:18px;border-radius:9px;background:linear-gradient(#4aa3ff,var(--blue-dark));color:#fff;font-size:9.5px;text-align:center;line-height:18px;text-decoration:none;box-shadow:0 1px 1px rgba(0,0,0,.25)}

/* feature band */
.feature-band{position:absolute;left:0;top:231px;width:675px;height:61px;background:var(--blue);display:flex;padding-left:74px}
.feature{position:relative;width:190px;padding:8px 0 0 29px;color:#fff}
.feature + .feature{border-left:1px solid rgba(255,255,255,.12)}
.feature:nth-child(2){width:185px;padding-left:43px}
.feature:nth-child(3){padding-left:47px}
.feature svg{position:absolute;left:0;top:6px}
.feature:nth-child(2) svg{left:22px}
.feature:nth-child(3) svg{left:19px}
.feature h3{font-size:13.5px;font-weight:400;line-height:14px}
.feature p{font-size:7.6px;line-height:10px;margin-top:3px;font-weight:700}

/* portfolio grid */
.work-grid{position:absolute;left:85px;top:319px;display:grid;grid-template-columns:repeat(3,148px);column-gap:29px;row-gap:27px}
.work-card{position:relative;height:142px;background:linear-gradient(#fff,#f2f2f2);border:1px solid #dedede;padding:3px}
.work-card::after{content:"";position:absolute;left:6px;right:6px;bottom:-6px;height:6px;background:radial-gradient(ellipse at top,rgba(0,0,0,.35),rgba(0,0,0,0) 70%)}
.work-thumb{height:82px}
.work-card h4{font-size:13px;font-weight:400;color:var(--blue);text-align:center;margin-top:5px;padding-bottom:1px;border-bottom:1px solid var(--line);margin-left:8px;margin-right:8px}
.work-card p{font-size:7.6px;line-height:9.5px;text-align:center;color:#333;margin-top:4px}
.t1{background:linear-gradient(135deg,#6f7b8c,#d8dde3 60%,#4d5868)}
.t2{background:linear-gradient(135deg,#3d3a3a,#c7b9ad 50%,#3a3f4a)}
.t3{background:linear-gradient(135deg,#cfe0ef,#58606d 55%,#e4e9ee)}
.t4{background:linear-gradient(135deg,#7890b0,#e9e6e2 55%,#434a56)}
.t5{background:linear-gradient(135deg,#e8eef4,#4f79b4 50%,#3b3f48)}
.t6{background:linear-gradient(135deg,#6c5a48,#d9cdbd 50%,#2f3036)}

/* info section */
.info{position:absolute;left:0;top:656px;width:675px;height:193px;background:var(--dark);border-top:3px solid #3b8cf7}
.info-cards{position:absolute;left:85px;top:25px;display:grid;grid-template-columns:repeat(3,148px);column-gap:29px}
.info-card{position:relative;height:139px;background:linear-gradient(#fff,#f0f0f0);padding-top:6px;text-align:center}
.info-card::after{content:"";position:absolute;left:6px;right:6px;bottom:-6px;height:6px;background:radial-gradient(ellipse at top,rgba(0,0,0,.6),rgba(0,0,0,0) 70%)}
.info-card h4{font-size:13px;font-weight:400;color:var(--blue);border-bottom:1px solid var(--line);margin:0 8px;padding-bottom:1px}
.info-card svg{display:block;margin:5px auto 2px}
.info-card p{font-size:7px;line-height:8.8px;color:#222;padding:0 8px}

/* footer */
.site-footer{position:absolute;left:0;top:849px;width:675px;height:30px;background:var(--footer)}
.copyright{position:absolute;left:87px;top:10px;font-size:7px;color:var(--footer-text)}
.footer-nav{position:absolute;right:87px;top:10px;display:flex;gap:11px}
.footer-nav a{font-size:7px;color:var(--footer-text);text-decoration:none}
.footer-nav a.active{color:#fff;font-weight:700}
</style>
</head>
<body>
<div class="page">

  <header class="site-header">
    <div class="brand"><span class="brand-dot"></span><span class="brand-name">vexlo</span></div>
    <nav class="main-nav">
      <a href="#">Home</a>
      <a href="#">About Us</a>
      <a href="#">Services</a>
      <a href="#" class="active">Portfolio</a>
      <a href="#">News</a>
      <a href="#">Contact Us</a>
    </nav>
  </header>

  <section class="hero">
    <svg class="hero-deco" width="675" height="173" viewBox="0 0 675 173">
      <circle cx="530" cy="150" r="140" fill="#e9e9eb"/>
      <circle cx="565" cy="165" r="125" fill="#ffffff"/>
      <path d="M600 45 Q660 60 675 120 L675 173 L640 173 Q640 90 600 45Z" fill="#e6eefb"/>
    </svg>
    <div class="hero-photo" role="img" aria-label="Photo of two business colleagues reviewing documents together"></div>
    <svg class="hero-arrow prev" viewBox="0 0 22 22"><circle cx="11" cy="11" r="10" fill="#2d3440" stroke="#5a9cf5" stroke-width="2"/><path d="M13 6 L8 11 L13 16" fill="none" stroke="#fff" stroke-width="2.4"/></svg>
    <svg class="hero-arrow next" viewBox="0 0 22 22"><circle cx="11" cy="11" r="10" fill="#2d3440" stroke="#5a9cf5" stroke-width="2"/><path d="M9 6 L14 11 L9 16" fill="none" stroke="#fff" stroke-width="2.4"/></svg>
    <div class="hero-copy">
      <h1 class="hero-title">Lorem <span>ipsum dolor</span></h1>
      <p class="hero-text">Sit amet, consectetur adipiscing elit. Nulla lobortis consequat mauris, eget eleifend</p>
    </div>
    <a href="#" class="btn-more">Read more</a>
  </section>

  <section class="feature-band">
    <div class="feature">
      <svg width="22" height="22" viewBox="0 0 22 22" fill="none" stroke="#1b1b1b" stroke-width="2"><circle cx="10" cy="10" r="8.5"/><path d="M1.5 10h17M10 1.5c-4 4-4 13 0 17M10 1.5c4 4 4 13 0 17"/><path d="M13 13l7 7" stroke-width="2.5"/></svg>
      <h3>Lorem ipsum dolor sit</h3>
      <p>Consectetur adipiscing elit. Nulla lobortis consequat mauris, eget eleifend nunc viverra viverra.</p>
    </div>
    <div class="feature">
      <svg width="16" height="22" viewBox="0 0 16 22" fill="none" stroke="#1b1b1b" stroke-width="1.8"><path d="M8 1a6.5 6.5 0 0 0-4 11.6V16h8v-3.4A6.5 6.5 0 0 0 8 1z"/><path d="M5 18h6M6 20.5h4"/></svg>
      <h3>Lorem ipsum dolor sit</h3>
      <p>Consectetur adipiscing elit. Nulla lobortis consequat mauris, eget eleifend nunc viverra viverra.</p>
    </div>
    <div class="feature">
      <svg width="22" height="22" viewBox="0 0 22 22" fill="none" stroke="#1b1b1b" stroke-width="2"><path d="M13 20H2V1h9l5 5v6"/><path d="M11 1v5h5"/><path d="M17 13v8M13 17h8" stroke-width="2.4"/></svg>
      <h3>Lorem ipsum dolor sit</h3>
      <p>Consectetur adipiscing elit. Nulla lobortis consequat mauris, eget eleifend nunc viverra viverra.</p>
    </div>
  </section>

  <section class="work-grid">
    <article class="work-card"><div class="work-thumb t1" role="img" aria-label="Photo of a team meeting seen from above"></div><h4>Lorem ipsum dolor sit</h4><p>Consectetur adipiscing elit. Nulla lobortis consequat mauris, eget</p></article>
    <article class="work-card"><div class="work-thumb t2" role="img" aria-label="Photo of colleagues talking at a table"></div><h4>Lorem ipsum dolor sit</h4><p>Consectetur adipiscing elit. Nulla lobortis consequat mauris, eget</p></article>
    <article class="work-card"><div class="work-thumb t3" role="img" aria-label="Photo of a business team in a bright office"></div><h4>Lorem ipsum dolor sit</h4><p>Consectetur adipiscing elit. Nulla lobortis consequat mauris, eget</p></article>
    <article class="work-card"><div class="work-thumb t4" role="img" aria-label="Photo of a group working around a laptop"></div><h4>Lorem ipsum dolor sit</h4><p>Consectetur adipiscing elit. Nulla lobortis consequat mauris, eget</p></article>
    <article class="work-card"><div class="work-thumb t5" role="img" aria-label="Photo of two coworkers at a desk"></div><h4>Lorem ipsum dolor sit</h4><p>Consectetur adipiscing elit. Nulla lobortis consequat mauris, eget</p></article>
    <article class="work-card"><div class="work-thumb t6" role="img" aria-label="Photo of a team reviewing papers in a meeting room"></div><h4>Lorem ipsum dolor sit</h4><p>Consectetur adipiscing elit. Nulla lobortis consequat mauris, eget</p></article>
  </section>

  <section class="info">
    <div class="info-cards">
      <article class="info-card">
        <h4>Lorem ipsum dolor sit</h4>
        <svg width="46" height="44" viewBox="0 0 46 44"><path d="M23 3C11 3 2 10 2 19c0 6 4 11 10 13l-2 9 9-7c1 0 3 .5 4 .5 12 0 21-7 21-15.5S35 3 23 3z" fill="#f7f7f7" stroke="#bdbdbd" stroke-width="1.5"/><rect x="21" y="9" width="4" height="14" rx="2" fill="#333"/><circle cx="23" cy="28" r="2.4" fill="#333"/></svg>
        <p>Nulla feugiat blandit. Cras vel libero ut lacus eleifend tempor. Phasellus eleifend, magna non tincidunt accumsan, justo arcu cursus ipsum, non porttitor sapien quam vel magna. Maecenas elit nisl, molestie nec dapibus nec,</p>
      </article>
      <article class="info-card">
        <h4>Lorem ipsum dolor sit</h4>
        <svg width="44" height="44" viewBox="0 0 44 44"><g fill="#f4f4f4" stroke="#bcbcbc" stroke-width="1.5"><path d="M19 2h6l1 6 4 2 5-4 4 4-4 5 2 4 6 1v6l-6 1-2 4 4 5-4 4-5-4-4 2-1 6h-6l-1-6-4-2-5 4-4-4 4-5-2-4-6-1v-6l6-1 2-4-4-5 4-4 5 4 4-2z"/><circle cx="22" cy="22" r="8" fill="#fff"/></g></svg>
        <p>Nulla feugiat blandit. Cras vel libero ut lacus eleifend tempor. Phasellus eleifend, magna non tincidunt accumsan, justo arcu cursus ipsum, non porttitor sapien quam vel magna. Maecenas elit nisl, molestie nec dapibus nec,</p>
      </article>
      <article class="info-card">
        <h4>Lorem ipsum dolor sit</h4>
        <svg width="40" height="44" viewBox="0 0 40 44"><path d="M4 4h26l6 6v30H4z" fill="#f1f1f1" stroke="#c4c4c4" stroke-width="1.5"/><path d="M30 4l6 6h-6z" fill="#2a7cf4"/><path d="M17 14h6v8h8v6h-8v8h-6v-8H9v-6h8z" fill="#111"/></svg>
        <p>Nulla feugiat blandit. Cras vel libero ut lacus eleifend tempor. Phasellus eleifend, magna non tincidunt accumsan, justo arcu cursus ipsum, non porttitor sapien quam vel magna. Maecenas elit nisl, molestie nec dapibus nec,</p>
      </article>
    </div>
  </section>

  <footer class="site-footer">
    <p class="copyright">Copyright information comes here</p>
    <nav class="footer-nav">
      <a href="#">Home</a>
      <a href="#">About Us</a>
      <a href="#">Services</a>
      <a href="#" class="active">Portfolio</a>
      <a href="#">News</a>
      <a href="#">Contact Us</a>
    </nav>
  </footer>

</div>
</body>
</html>
```